Business Card and Letterhead Design for Public Accounting Firm

Business card and letterhead design for a CPA Firm located in Orange County, CA. We're looking for a modern and professional design utilizing our existing logo. We'd like a clean "less is more" look, but also something that catches the eye. We provide a high level of service to our clients. Open to single or double sided business cards.

Additional info: color numbers on logo
Blue :
R 0
G 83
B 125

#00537D

Silver :

R 154
G 154
B 154

#9A9A9A

Target Market(s)

Businesses and individuals

Industry/Entity Type

Accounting

Contact Information for Business Card

Moss Whitfield & Danby LLP - 4827 Larkspur Vale Road, Irvine, CA 92614 - (949)731-2864 - mwdaccts.example

Font styles to use
Serif
Sans Serif
Other font styles liked:
• See font file uploaded

Colors
0054AA
0677BA
7BADD7
CADEEF
E8F1F8

Requirements
Nice to have
• Possibly use the font file provided which matches our logo, but adjust to be not in all caps

```html
<!DOCTYPE html>
<html lang="en">
<head>
<meta charset="utf-8">
<title>Moss Whitfield &amp; Danby LLP — Business Card</title>
<link rel="stylesheet" href="https://fonts.googleapis.com/css2?family=Cinzel:wght@400;600&display=swap">
<style>
  :root {
    --brand-blue: #00537d;
    --brand-blue-deep: #004a70;
    --brand-silver: #9a9a9a;
    --band-grey: #a3a3a3;
    --card-white: #ffffff;
    --page-bg: #e9ecef;
    --text-blue: #0d4f78;
  }
  * { box-sizing: border-box; margin: 0; padding: 0; }
  html, body { width: 1200px; height: 900px; overflow: hidden; }
  body {
    background: var(--page-bg);
    font-family: "Cinzel", "Times New Roman", serif;
    position: relative;
  }
  .card {
    position: absolute;
    left: 250px;
    width: 700px;
    height: 400px;
    border-radius: 2px;
    box-shadow: 0 6px 18px rgba(0,0,0,0.18);
    overflow: hidden;
  }
  /* Back side */
  .card-back {
    top: 35px;
    background: linear-gradient(135deg, #0a5c88 0%, var(--brand-blue-deep) 100%);
  }
  .card-back .back-field {
    position: absolute; inset: 0;
    background: linear-gradient(160deg, rgba(255,255,255,0.05), rgba(255,255,255,0));
  }
  .card-back .back-name {
    position: absolute;
    right: 90px;
    bottom: 150px;
    font-size: 40px;
    font-weight: 600;
    color: #e8ecef;
    letter-spacing: 1px;
  }
  /* Front side */
  .card-front {
    top: 465px;
    background: var(--card-white);
  }
  .firm-lockup {
    position: absolute;
    left: 48px;
    top: 52px;
    display: flex;
    align-items: center;
  }
  .firm-mark {
    font-size: 38px;
    font-weight: 600;
    color: var(--brand-blue);
    letter-spacing: 1px;
  }
  .firm-divider {
    width: 1px;
    height: 46px;
    background: var(--brand-silver);
    margin: 0 12px;
  }
  .firm-name {
    font-size: 15px;
    line-height: 18px;
    color: #6d7f8c;
    letter-spacing: 2px;
  }
  .person {
    position: absolute;
    left: 52px;
    top: 196px;
  }
  .person-name {
    font-size: 30px;
    color: var(--text-blue);
    letter-spacing: 1.5px;
  }
  .person-title {
    font-size: 12px;
    color: var(--brand-silver);
    letter-spacing: 6px;
    margin-top: 2px;
  }
  .contact {
    position: absolute;
    left: 52px;
    top: 270px;
    font-size: 17px;
    line-height: 24px;
    color: var(--text-blue);
    letter-spacing: 1px;
  }
  .contact .label { color: var(--brand-silver); margin-right: 8px; }
  .card-bands {
    position: absolute; left: 0; top: 0;
  }
  .address {
    position: absolute;
    left: 40px;
    top: 348px;
    height: 52px;
    display: flex;
    align-items: center;
    font-size: 17px;
    color: #ffffff;
    letter-spacing: 1px;
    white-space: nowrap;
  }
  .website {
    position: absolute;
    right: 20px;
    top: 296px;
    height: 52px;
    display: flex;
    align-items: center;
    font-size: 13px;
    color: #ffffff;
    letter-spacing: 1px;
    white-space: nowrap;
  }
</style>
</head>
<body>
  <section class="card card-back" aria-label="Card back">
    <div class="back-field" role="img" aria-label="Blue background field"></div>
    <div class="back-name">MW&amp;D</div>
  </section>

  <section class="card card-front" aria-label="Card front">
    <svg class="card-bands" width="700" height="400" viewBox="0 0 700 400" aria-hidden="true">
      <polygon points="0,348 488,348 460,400 0,400" fill="#a3a3a3"/>
      <polygon points="524,296 700,296 700,348 496,348" fill="#00537d"/>
    </svg>

    <div class="firm-lockup">
      <div class="firm-mark">MW&amp;D</div>
      <div class="firm-divider"></div>
      <div class="firm-name">MOSS WHITFIELD<br>&amp; DANBY LLP</div>
    </div>

    <div class="person">
      <div class="person-name">Daniel Harrow</div>
      <div class="person-title">MANAGING DIRECTOR</div>
    </div>

    <div class="contact">
      <div><span class="label">P</span>(949) 731 2864</div>
      <div><span class="label">E</span>info@mwdaccts.example</div>
    </div>

    <div class="address">4827 Larkspur Vale Road, Irvine, CA 92614</div>
    <div class="website">MWDACCTS.EXAMPLE</div>
  </section>
</body>
</html>
```